Design for Cedar Lark Homes real estate agency

Incorporate logo into new business cards. I need to include the Brindley Vance logo incorporated into Cedar Lark Homes on one side of the card (attached). On the other side I see just the icon with "Maren Quill" (attached) with "Guided by Integrity" either included as is or removed from logo and rather put as a tag line on the business card separate from the main logo. Contact information:

Maren Quill
Associate Broker
Cell: 730-418-5093
Email: marenquill@cedarlarkhomes.example
Web: www.cedarlarkhomes.example

Target Market(s)

Buyers, Sellers, Builders and Investors of homes and land

Industry/Entity Type

Real Estate Agent

Contact Information for Business Card

My client base tend to be higher end home buyers, sellers, builders and investors. I have been more and more in land and subdivisions for builders and investors. The card should not be cluttered. Clean and simple - yet with an air of exclusive/high end

Colors

Designer to choose colors to be used in the design.

Requirements
Must have
• Must have the logo on one side that has Brindley Vance logo incorporated. The side that has my contact information does not have to have the Brindley Vance logo incorporated.
• Must include "Guided by Integrity" tag line either within logo (as is) or removed from logo and included in another position on the side of the business card with contact information.
Should not have
• Should not have Brindley Vance logo incorporated into Cedar Lark Homes logo on both sides of business card. Would like the Cedar Lark Homes logo that has Brindley Logo only on the back side of card without contact information.

```html
<!DOCTYPE html>
<html lang="en">
<head>
<meta charset="utf-8">
<title>Maren Quill — Cedar Lark Homes Business Card</title>
<link href="https://fonts.googleapis.com/css2?family=Cinzel:wght@600&family=Playfair+Display:wght@700&family=Lato:wght@400;700;900&display=swap" rel="stylesheet">
<style>
  :root {
    --backdrop: #1c1c1c;
    --card: #f7f6f3;
    --brown: #6e5632;
    --brown-dark: #4a3a22;
    --gold: #cfae3c;
    --gold-soft: #e2c766;
    --ink: #3d3a36;
  }
  * { box-sizing: border-box; margin: 0; padding: 0; }
  html, body { width: 1200px; height: 900px; overflow: hidden; }
  body {
    background: var(--backdrop);
    display: flex;
    flex-direction: column;
    align-items: center;
    justify-content: center;
    gap: 40px;
  }
  .card {
    position: relative;
    width: 700px;
    height: 400px;
    background: var(--card);
    border-radius: 16px;
    overflow: hidden;
  }

  /* Contact side */
  .signature {
    position: absolute;
    left: 56px;
    top: 52px;
    color: var(--brown);
  }
  .signature__name {
    font-family: "Cinzel", serif;
    font-weight: 600;
    font-size: 38px;
    letter-spacing: 0.18em;
  }
  .signature__tagline {
    font-family: "Lato", sans-serif;
    font-size: 11px;
    letter-spacing: 0.42em;
    text-transform: uppercase;
    margin-top: 2px;
    padding-left: 4px;
  }
  .agent {
    position: absolute;
    left: 56px;
    top: 178px;
    font-family: "Lato", sans-serif;
  }
  .agent__name {
    font-weight: 900;
    font-size: 28px;
    color: var(--brown-dark);
  }
  .agent__title {
    font-weight: 400;
    font-size: 20px;
    color: var(--gold);
    margin-top: 2px;
  }
  .contacts {
    list-style: none;
    margin-top: 20px;
    font-size: 15px;
    color: var(--ink);
  }
  .contacts li {
    display: flex;
    align-items: center;
    gap: 10px;
    margin-bottom: 6px;
  }
  .contacts svg { width: 14px; height: 14px; fill: var(--brown-dark); flex: none; }
  .brand-mark {
    position: absolute;
    right: 70px;
    bottom: 44px;
    width: 170px;
    height: 170px;
    border-radius: 50%;
    background: radial-gradient(circle at 40% 40%, var(--gold-soft), var(--gold) 70%);
  }

  /* Brand side */
  .card--brand {
    display: flex;
    align-items: center;
    justify-content: center;
  }
  .lockup {
    display: flex;
    align-items: center;
    gap: 22px;
  }
  .lockup__dot {
    width: 70px;
    height: 70px;
    border-radius: 50%;
    background: var(--gold);
    flex: none;
  }
  .lockup__text { color: var(--brown); }
  .lockup__company {
    font-family: "Playfair Display", serif;
    font-weight: 700;
    font-size: 50px;
    line-height: 1;
  }
  .lockup__row {
    display: flex;
    align-items: center;
    gap: 14px;
    margin-top: 10px;
  }
  .lockup__rule {
    flex: 1;
    height: 2px;
    background: var(--brown);
  }
  .lockup__agent {
    font-family: "Cinzel", serif;
    font-weight: 600;
    font-size: 18px;
    letter-spacing: 0.2em;
    text-align: right;
  }
  .lockup__tagline {
    font-family: "Lato", sans-serif;
    font-size: 9px;
    letter-spacing: 0.4em;
    text-transform: uppercase;
    text-align: right;
  }
  .partner-badge {
    width: 64px;
    height: 38px;
    background: var(--brown);
    border-radius: 2px;
    flex: none;
  }
</style>
</head>
<body>
  <section class="card card--contact">
    <div class="signature">
      <div class="signature__name">MAREN QUILL</div>
      <div class="signature__tagline">Guided by Integrity</div>
    </div>

    <div class="agent">
      <div class="agent__name">Maren Quill</div>
      <div class="agent__title">Associate Broker</div>
      <ul class="contacts">
        <li>
          <svg viewBox="0 0 24 24" aria-hidden="true"><path d="M6.6 10.8a15.1 15.1 0 0 0 6.6 6.6l2.2-2.2c.3-.3.7-.4 1-.2 1.1.4 2.3.6 3.6.6.6 0 1 .4 1 1V20c0 .6-.4 1-1 1A17 17 0 0 1 3 4c0-.6.4-1 1-1h3.5c.6 0 1 .4 1 1 0 1.3.2 2.5.6 3.6.1.3 0 .7-.2 1z"/></svg>
          730-418-5093
        </li>
        <li>
          <svg viewBox="0 0 24 24" aria-hidden="true"><path d="M2 5h20v14H2zm2 2v.5l8 5 8-5V7l-8 5z"/></svg>
          marenquill@cedarlarkhomes.example
        </li>
        <li>
          <svg viewBox="0 0 24 24" aria-hidden="true"><path d="M12 2a10 10 0 1 0 0 20 10 10 0 0 0 0-20zm6.9 6h-3a15 15 0 0 0-1.3-3.9A8 8 0 0 1 18.9 8zM12 4c.8 1.2 1.5 2.5 1.9 4h-3.8c.4-1.5 1.1-2.8 1.9-4zM4.3 14a8 8 0 0 1 0-4h3.4a16 16 0 0 0 0 4zm.8 2h3a15 15 0 0 0 1.3 3.9A8 8 0 0 1 5.1 16zm3-8h-3a8 8 0 0 1 4.3-3.9A15 15 0 0 0 8.1 8zM12 20c-.8-1.2-1.5-2.5-1.9-4h3.8c-.4 1.5-1.1 2.8-1.9 4zm2.3-6H9.7a14 14 0 0 1 0-4h4.6a14 14 0 0 1 0 4zm.3 5.9a15 15 0 0 0 1.3-3.9h3a8 8 0 0 1-4.3 3.9zm1.7-5.9a16 16 0 0 0 0-4h3.4a8 8 0 0 1 0 4z"/></svg>
          www.cedarlarkhomes.example
        </li>
      </ul>
    </div>

    <div class="brand-mark" role="img" aria-label="Cedar Lark Homes brand mark"></div>
  </section>

  <section class="card card--brand">
    <div class="lockup">
      <div class="lockup__dot" aria-hidden="true"></div>
      <div class="lockup__text">
        <div class="lockup__company">Cedar Lark Homes</div>
        <div class="lockup__row">
          <div class="lockup__rule"></div>
          <div>
            <div class="lockup__agent">MAREN QUILL</div>
            <div class="lockup__tagline">Guided by Integrity</div>
          </div>
          <div class="partner-badge" role="img" aria-label="Brindley Vance partner badge"></div>
        </div>
      </div>
    </div>
  </section>
</body>
</html>
```